Honey Label for a private beekeeper

I am an "amateur" beekeeper and like to promote and sell my honey. The target group is anyone who likes honey. Task: The label design should basically be an "eye-catcher" and express the high quality of the natural product honey. In the narrower sense, but which should form a unit in the design: The first part is the so-called guaranty; he connects with the glass and tears when first opening the lid. The lock should be about 2 inches wide and 8 inches long, and adorned by the words 'The best of the nature'. In brackets you always find the english translation of the german text for a better understanding. The second part is the product label. For this there are no shape specifications but max. height is 5cm and maximum is 12cm (for 500g jar), but the following must be included in the account: "Please use the following placeholders", "first name last name", "street house number", "post code city name ") as well as the words" 500g "," Best Before Date ", (" Best before "), behind or below please leave blank space for the stamp imprint of the date," Store dry, dark and protected from heat! dry, dark and protected from heat), And - most important - the text: "Finest bee honey" and in new line "from Cologne - Porz (from Cologne - Porz)" as well as the two varieties "Summer Blossom" or "Spring Blossom" ... in the future may be added more varieties. The company logo should be used in a single color, so that the customer can quickly identify the type of honey in the glass. For this purpose, the respective honeysuckle color, in whatever form, dominate the label or a certain area of ​​it. I have uploaded a few labels from the internet that appealed to me about their style, but it's definitely not about making just one copy of one of these labels. Please use the german text on the label, the translation is just for you. Please contact me in case of any further questions or problems with my explanation. I'm looking forward to your designs! As an 'amateur' I run a hobby-beekeeping and want to drive out my evening gown and summer turkey honey. The target group is anyone who likes honey. Task The Etiketten_Design to be designed should basically be an "eye-catcher", have a high recognition value and express the high quality of the natural product honey. In the narrower sense, two independent parts of the label are to be designed, but which should form a unit in the design: The first part is the so-called warranty; he connects the lid with the glass and tears when first opening the lid. The lock should be about 2 cm wide and 8 cm long, and adorned by the saying 'the best of nature'. The second part is the actual product label. For this there are no size and shape specifications, but the following contents must be considered: The data of the beekeeper (please use the following placeholders "first name last name", "street house number", "ZIP place name") and the information "500g", "At least Best before: "(behind or below, please leave white space for the stamp imprint of the date)," dry, dark and protect from heat! ", and - most importantly - the text: finest bee honey (new line) from Cologne - Porz as well the two denominations spring blossom or summer bloom (in the future may be added more varieties). The logo of the company should be used, but it can also be used on the freshly-baked seal (see appendix) Each type of honey (summer blossom and spring blossom) should be associated with a color, so that the customer can quickly identify which type of honey is in the glass. For this, the respective honeysuckle color, in whatever form, should dominate the label or a certain area of ​​it. With regard to a good reproducibility of the labels in large quantities, we ask for the following further requirements to be observed: • Please place text and picture elements with 4mm distance to the label edges. • Please consider the CYMK color scheme. • If you choose multicolored labels, please use a maximum of four colors. • The honeysuckle color of the product label should NOT be found on the warranty seal (because the guarantee applies generally to any honey jar, regardless of the honeys). • The product label should be editable. • The product label should be scalable (for both small 250g glasses and large 500g glasses). The last two points can be ignored if a larger copy with the indication "500g" and a smaller one with the indication "250g" are created per product label. I'm looking forward to your designs!

Target Market(s)

Neighborhood and shops

Colors

Designer to choose colors to be used in the design.

Requirements
Must have
• With regard to the following further requirements: • Please place text and picture elements 4mm from the edges of the labels. • Please consider the CYMK color scheme. • If you choose multicolored labels, please use a maximum of four colors. The honeysuckle color of the product label should not be found on the warranty. • The product label should be editable. • The product label needs to be scalable The "500g" and the smaller "250g" are created by product label.
Should not have
• Please do not use the color gold no transparent labels

```html
<!DOCTYPE html>
<html lang="de">
<head>
<meta charset="utf-8">
<title>Honigetiketten – Feinster Bienenhonig</title>
<link rel="stylesheet" href="https://fonts.googleapis.com/css2?family=Montserrat:wght@500;700&family=Parisienne&display=swap">
<style>
  :root {
    --canvas: #999999;
    --white: #ffffff;
    --ink: #222222;
    --brand: #f5b400;

    --spring-bg: #c4ebc9;
    --spring-box: #8dd0ab;
    --spring-tag: #5c9d86;
    --spring-addr: #4f8f72;

    --summer-bg: #ffd48a;
    --summer-box: #fd8b22;
    --summer-tag: #cc1212;
    --summer-addr: #5a1a2a;

    --generic-bg: #a8e0de;
    --generic-box: #7cc3c4;
    --generic-tag: #2f7b8a;
    --generic-addr: #2a5fa0;
  }
  * { box-sizing: border-box; margin: 0; padding: 0; }
  html, body { width: 1200px; height: 1200px; overflow: hidden; }
  body { background: var(--canvas); position: relative; font-family: "Montserrat", sans-serif; }

  .label {
    position: absolute; left: 266px; width: 671px; height: 280px;
    background: var(--bg); overflow: hidden;
  }
  .label--spring  { top: 80px;  --bg: var(--spring-bg);  --box: var(--spring-box);  --tag: var(--spring-tag);  --addr: var(--spring-addr); }
  .label--summer  { top: 466px; --bg: var(--summer-bg);  --box: var(--summer-box);  --tag: var(--summer-tag);  --addr: var(--summer-addr); }
  .label--generic { top: 860px; --bg: var(--generic-bg); --box: var(--generic-box); --tag: var(--generic-tag); --addr: var(--generic-addr); }

  .label__pattern { position: absolute; inset: 0; width: 671px; height: 280px; }

  .producer {
    position: absolute; left: 16px; top: 28px; width: 145px; height: 144px;
    background: var(--white); text-align: center;
  }
  .brand {
    display: flex; align-items: center; justify-content: center; gap: 5px;
    margin-top: 26px; height: 60px; flex-direction: column;
  }
  .brand__dot { width: 34px; height: 34px; border-radius: 50%; background: var(--brand); }
  .brand__name { font-size: 10px; font-weight: 700; color: var(--brand); letter-spacing: 0.5px; }
  .producer__address {
    margin-top: 12px; font-size: 10.5px; line-height: 12.5px; font-weight: 500;
    color: var(--addr); letter-spacing: 0.3px;
  }

  .storage {
    position: absolute; left: 16px; top: 176px; width: 145px; height: 86px;
    background: var(--box); text-align: center; color: var(--white);
  }
  .storage__note {
    font-size: 8px; font-weight: 700; line-height: 11px; color: var(--ink);
    padding: 8px 2px 6px; border-bottom: 1px solid rgba(255,255,255,0.5);
    opacity: 0.85;
  }
  .storage__bbd-label { font-size: 8.5px; font-weight: 700; letter-spacing: 0.4px; margin-top: 6px; }
  .storage__stamp { margin: 5px auto 0; width: 133px; height: 19px; background: var(--white); }

  .title {
    position: absolute; left: 198px; width: 440px; top: 38px; text-align: center;
    font-family: "Parisienne", cursive; font-size: 36px; font-weight: 400;
    color: var(--ink); line-height: 1; white-space: nowrap;
  }
  .origin {
    position: absolute; left: 218px; width: 400px; top: 85px; text-align: center;
    font-size: 15.5px; letter-spacing: 3.2px; color: var(--ink); font-weight: 500;
    white-space: nowrap;
  }
  .variety {
    position: absolute; left: 418px; transform: translateX(-50%);
    top: 205px; background: var(--tag); color: var(--white);
    font-size: 17px; font-weight: 700; letter-spacing: 2.6px; padding: 3px 14px 2px;
    white-space: nowrap;
  }
  .weight {
    position: absolute; left: 268px; width: 300px; top: 236px; text-align: center;
    font-size: 17px; font-weight: 700; color: var(--ink);
  }

  .seal {
    position: absolute; left: 1046px; top: 381px; width: 65px; height: 435px;
    background: var(--white);
  }
  .seal__motto {
    position: absolute; left: 32px; top: 160px; transform: translate(-50%, -50%) rotate(-90deg);
    white-space: nowrap; font-size: 13.5px; letter-spacing: 2.6px; color: var(--ink); font-weight: 500;
  }
  .seal__mark { position: absolute; left: 17px; top: 390px; }
</style>
</head>
<body>

<section class="label label--spring">
  <svg class="label__pattern" viewBox="0 0 671 280" role="img" aria-label="Wabenmuster in Frühlingsgrün">
    <path fill="#ffffff" d="M150 0 H671 V40 C650 70 620 90 590 100 C560 110 540 125 500 135 C430 145 340 148 290 135 C250 122 200 112 170 75 C158 50 150 30 150 0 Z"/>
  </svg>
  <div class="producer">
    <div class="brand"><span class="brand__dot"></span><span class="brand__name">IMKEREI LINDNER</span></div>
    <p class="producer__address">Max Mustermann<br>Musterstraße 12<br>34567 Musterstadt</p>
  </div>
  <div class="storage">
    <p class="storage__note">TROCKEN, DUNKEL UND VOR<br>WÄRME GESCHÜTZT LAGERN</p>
    <p class="storage__bbd-label">MIND. HALTBAR BIS:</p>
    <div class="storage__stamp"></div>
  </div>
  <h1 class="title">Feinster Bienenhonig</h1>
  <p class="origin">AUS KÖLN-PORZ</p>
  <p class="variety">FRÜHLINGSBLÜTE</p>
  <p class="weight">500g</p>
</section>

<section class="label label--summer">
  <svg class="label__pattern" viewBox="0 0 671 280" role="img" aria-label="Wabenmuster in Sommergelb">
    <path fill="#ffffff" d="M150 0 H671 V40 C650 70 620 90 590 100 C560 110 540 125 500 135 C430 145 340 148 290 135 C250 122 200 112 170 75 C158 50 150 30 150 0 Z"/>
  </svg>
  <div class="producer">
    <div class="brand"><span class="brand__dot"></span><span class="brand__name">IMKEREI LINDNER</span></div>
    <p class="producer__address">Max Mustermann<br>Musterstraße 12<br>34567 Musterstadt</p>
  </div>
  <div class="storage">
    <p class="storage__note">TROCKEN, DUNKEL UND VOR<br>WÄRME GESCHÜTZT LAGERN</p>
    <p class="storage__bbd-label">MIND. HALTBAR BIS:</p>
    <div class="storage__stamp"></div>
  </div>
  <h1 class="title">Feinster Bienenhonig</h1>
  <p class="origin">AUS KÖLN-PORZ</p>
  <p class="variety">SOMMERBLÜTE</p>
  <p class="weight">500g</p>
</section>

<section class="label label--generic">
  <svg class="label__pattern" viewBox="0 0 671 280" role="img" aria-label="Wabenmuster in Türkis">
    <path fill="#ffffff" d="M150 0 H671 V40 C650 70 620 90 590 100 C560 110 540 125 500 135 C430 145 340 148 290 135 C250 122 200 112 170 75 C158 50 150 30 150 0 Z"/>
  </svg>
  <div class="producer">
    <div class="brand"><span class="brand__dot"></span><span class="brand__name">IMKEREI LINDNER</span></div>
    <p class="producer__address">Max Mustermann<br>Musterstraße 12<br>34567 Musterstadt</p>
  </div>
  <div class="storage">
    <p class="storage__note">TROCKEN, DUNKEL UND VOR<br>WÄRME GESCHÜTZT LAGERN</p>
    <p class="storage__bbd-label">MIND. HALTBAR BIS:</p>
    <div class="storage__stamp"></div>
  </div>
  <h1 class="title">Feinster Bienenhonig</h1>
  <p class="origin">AUS KÖLN-PORZ</p>
  <p class="variety">PLATZHALTER</p>
  <p class="weight">500g</p>
</section>

<aside class="seal">
  <p class="seal__motto">DAS BESTE AUS DER NATUR</p>
  <svg class="seal__mark" width="31" height="27" viewBox="0 0 31 27">
    <polygon points="8,1 23,1 30,13.5 23,26 8,26 1,13.5" fill="none" stroke="#222222" stroke-width="1.2"/>
  </svg>
</aside>

</body>
</html>
```